Create a modern 3D / isometric infographic for a software diagram

Hello,
We are looking for a drawing of a software platform/application. This infographic should be be simple, modern, clean and lay-out how our software works. We need for someone to take these abstract concepts and put them into a concrete illustration style (3D / isometric style preferred).
The drawing should show the connections between the platform sections, and show that the platform is secure. Platform components can be presented with words or symbols.
This graphic asset will be used on our website, as well as presentation slides. Made to use on a white background.
I've uploaded a 2 examples of illustration styles I like, as well as a rough diagram of our software broken down,
See image attached.
Updates
Need extra days to review
Target Market(s)
Corporate
Industry/Entity Type
Mining
Font styles to use
Other font styles liked:
- Roboto

```html
<!DOCTYPE html>
<html lang="en">
<head>
<meta charset="utf-8">
<title>Platform Architecture Overview</title>
<link rel="stylesheet" href="https://fonts.googleapis.com/css2?family=Poppins:wght@400;700&display=swap">
<style>
  :root {
    --green: #8dc63f;
    --green-dark: #6f9a3a;
    --green-light: #d6ecb4;
    --navy: #14324f;
    --shadow: #e1e1e3;
    --face: #f6fafd;
    --white: #ffffff;
  }
  html, body {
    margin: 0;
    padding: 0;
    width: 1200px;
    height: 848px;
    overflow: hidden;
    background: var(--white);
  }
  .canvas {
    position: relative;
    width: 1200px;
    height: 848px;
  }
  .diagram {
    position: absolute;
    inset: 0;
    width: 1200px;
    height: 848px;
  }
  .tile-label {
    font-family: "Poppins", sans-serif;
    font-weight: 700;
    font-size: 26px;
    fill: var(--navy);
    text-anchor: middle;
  }
  .core-label {
    font-family: "Poppins", sans-serif;
    font-weight: 700;
    font-size: 40px;
    fill: var(--green);
    text-anchor: middle;
  }
  .link-green { fill: none; stroke: var(--green); stroke-width: 3; stroke-dasharray: 10 9; }
  .link-navy { fill: none; stroke: var(--navy); stroke-width: 3; stroke-dasharray: 8 9; }
  .legend {
    position: absolute;
    left: 99px;
    top: 768px;
    font-family: "Poppins", sans-serif;
    font-size: 17px;
    list-style: none;
    margin: 0;
    padding: 0;
  }
  .legend-item {
    display: flex;
    align-items: center;
    height: 18px;
    margin-bottom: 11px;
  }
  .legend-swatch {
    width: 25px;
    height: 17px;
    margin-right: 25px;
  }
  .legend-item--ours { color: var(--green); }
  .legend-item--ours .legend-swatch { background: var(--green); }
  .legend-item--other { color: var(--navy); }
  .legend-item--other .legend-swatch { background: var(--navy); }
</style>
</head>
<body>
<main class="canvas">
<svg class="diagram" viewBox="0 0 2287 1616" preserveAspectRatio="xMidYMid meet" xmlns="http://www.w3.org/2000/svg">
  <defs>
    <linearGradient id="side-navy" x1="0" y1="0" x2="0" y2="1">
      <stop offset="0" stop-color="#f4f6fa"/>
      <stop offset="1" stop-color="#6b6e8c"/>
    </linearGradient>
    <linearGradient id="side-green" x1="0" y1="0" x2="0" y2="1">
      <stop offset="0" stop-color="#f6faf0"/>
      <stop offset="1" stop-color="#b4db72"/>
    </linearGradient>
    <linearGradient id="device-glass" x1="0" y1="0" x2="1" y2="1">
      <stop offset="0" stop-color="#f6fbf0"/>
      <stop offset="1" stop-color="#e4f1d2"/>
    </linearGradient>

    <g id="tile-navy">
      <path d="M10,-40 L100,12 L100,62 L10,114 L-80,62 L-80,12 Z" fill="var(--shadow)"/>
      <path d="M0,-52 L90,0 L90,50 L0,102 L-90,50 L-90,0 Z" fill="url(#side-navy)" stroke="var(--navy)" stroke-width="8" stroke-linejoin="round"/>
      <path d="M0,-52 L90,0 L0,52 L-90,0 Z" fill="var(--face)"/>
    </g>
    <g id="tile-green">
      <path d="M10,-40 L100,12 L100,62 L10,114 L-80,62 L-80,12 Z" fill="var(--shadow)"/>
      <path d="M0,-52 L90,0 L90,50 L0,102 L-90,50 L-90,0 Z" fill="url(#side-green)" stroke="var(--green)" stroke-width="8" stroke-linejoin="round"/>
      <path d="M0,-52 L90,0 L0,52 L-90,0 Z" fill="var(--face)"/>
    </g>
  </defs>

  <!-- connections -->
  <g class="links">
    <polyline class="link-green" points="600,545 1000,770"/>
    <polyline class="link-green" points="370,670 460,725 640,625 1010,835"/>
    <polyline class="link-navy" points="1290,495 975,680 1000,700"/>
    <polyline class="link-navy" points="1170,430 1090,385"/>
    <polyline class="link-green" points="1350,955 1465,1015 1640,915"/>
    <polyline class="link-green" points="1320,980 1535,1100 1745,980"/>
    <polyline class="link-navy" points="1280,995 1680,1220"/>
    <polyline class="link-navy" points="1790,1290 1860,1330"/>
    <polyline class="link-green" points="1230,1030 1305,1075 1045,1220"/>
    <polyline class="link-green" points="1260,1020 1425,1125 1150,1285"/>
    <polyline class="link-green" points="1290,1005 1585,1190 1285,1365"/>
  </g>

  <!-- client devices -->
  <g class="device device--tablet">
    <path d="M200,700 L470,545 Q500,560 490,620 L290,750 Q230,760 200,700 Z" fill="var(--shadow)"/>
    <path d="M215,440 Q215,420 235,410 L430,312 Q460,300 460,335 L460,600 Q460,618 440,630 L250,728 Q215,740 215,710 Z" fill="url(#device-glass)" stroke="var(--green)" stroke-width="9" stroke-linejoin="round"/>
    <path d="M240,470 L440,365 L440,590 L240,695 Z" fill="#cfe7a8" opacity="0.7" role="img" aria-label="Configuration gears illustration"/>
  </g>
  <g class="device device--phone">
    <path d="M490,570 L700,460 Q730,480 710,510 L540,605 Q500,612 490,570 Z" fill="var(--shadow)"/>
    <path d="M487,195 Q487,160 520,145 L650,78 Q678,70 678,100 L678,470 Q678,490 655,502 L525,568 Q487,585 487,545 Z" fill="#cfe7a8" stroke="var(--green)" stroke-width="6" stroke-linejoin="round"/>
    <path d="M510,185 Q510,168 528,158 L650,97 Q670,90 670,108 L670,480 Q670,492 655,500 L530,562 Q510,570 510,550 Z" fill="var(--face)" stroke="var(--green)" stroke-width="6" stroke-linejoin="round"/>
  </g>

  <!-- other software modules -->
  <g class="module-grid">
    <use href="#tile-navy" x="1045" y="140"/>
    <text class="tile-label" transform="translate(1048,148) rotate(-30)">FMS</text>
    <use href="#tile-navy" x="915" y="215"/>
    <text class="tile-label" transform="translate(918,200) rotate(-30)"><tspan x="0" dy="-8">MAIN</tspan><tspan x="0" dy="27">TENA</tspan><tspan x="0" dy="27">NCE</tspan></text>
    <use href="#tile-navy" x="1175" y="215"/>
    <text class="tile-label" transform="translate(1175,225) rotate(-30)">ERP</text>
    <use href="#tile-navy" x="787" y="290"/>
    <text class="tile-label" transform="translate(790,288) rotate(-30)"><tspan x="0" dy="-6">PLAN</tspan><tspan x="0" dy="28">NING</tspan></text>
    <use href="#tile-navy" x="1045" y="290"/>
    <text class="tile-label" transform="translate(1045,288) rotate(-30)"><tspan x="0" dy="-6">SCA</tspan><tspan x="0" dy="28">DA</tspan></text>
    <use href="#tile-navy" x="915" y="365"/>
    <text class="tile-label" transform="translate(915,375) rotate(-30)">LIMS</text>
  </g>

  <!-- connectors -->
  <g class="connector connector--etl">
    <ellipse cx="1230" cy="425" rx="58" ry="86" transform="rotate(30 1230 425)" fill="var(--navy)"/>
    <ellipse cx="1245" cy="415" rx="58" ry="86" transform="rotate(30 1245 415)" fill="var(--face)" stroke="var(--navy)" stroke-width="8"/>
    <text class="tile-label" font-size="32" transform="translate(1253,428) rotate(-30)">ETL</text>
  </g>
  <g class="connector connector--api">
    <ellipse cx="1735" cy="1240" rx="58" ry="86" transform="rotate(30 1735 1240)" fill="var(--navy)"/>
    <ellipse cx="1750" cy="1230" rx="58" ry="86" transform="rotate(30 1750 1230)" fill="var(--face)" stroke="var(--navy)" stroke-width="8"/>
    <text class="tile-label" font-size="32" transform="translate(1758,1243) rotate(-30)">API</text>
  </g>

  <!-- core platform -->
  <g class="core">
    <path d="M990,1010 L1180,900 L1370,1010 L1180,1115 Z" fill="var(--shadow)"/>
    <path d="M965,880 L1180,760 L1395,880 L1395,920 L1180,1040 L965,920 Z" fill="var(--green-dark)" stroke="var(--green)" stroke-width="7" stroke-linejoin="round"/>
    <path d="M965,880 L1180,760 L1395,880 L1180,1000 Z" fill="var(--green-dark)"/>
    <path d="M1010,880 L1180,785 L1350,880 L1180,975 Z" fill="var(--green-light)"/>
    <path d="M1045,880 L1180,805 L1315,880 L1180,955 Z" fill="var(--green)"/>
    <path d="M965,750 L1180,628 L1395,750 L1395,780 L1180,902 L965,780 Z" fill="url(#side-green)" stroke="var(--green)" stroke-width="7" stroke-linejoin="round"/>
    <path d="M965,750 L1180,628 L1395,750 L1180,872 Z" fill="var(--face)" stroke="var(--green)" stroke-width="5" stroke-linejoin="round"/>
    <path d="M1025,750 L1180,662 L1335,750 L1180,838 Z" fill="none" stroke="var(--green)" stroke-width="3" stroke-linejoin="round"/>
    <text class="core-label" transform="translate(1170,745) rotate(-30)"><tspan x="0" dy="0">NORTHLINE</tspan><tspan x="20" dy="44">CORE</tspan></text>
  </g>

  <!-- our software modules -->
  <g class="modules-ours">
    <use href="#tile-green" x="1700" y="830"/>
    <use href="#tile-green" x="1822" y="905"/>
    <g transform="translate(1822,903) scale(1,0.58) rotate(45)" fill="none" stroke="var(--green)">
      <circle r="30" stroke-width="14" stroke-dasharray="12 11"/>
      <circle r="22" stroke-width="12"/>
    </g>
    <use href="#tile-green" x="980" y="1255"/>
    <g transform="translate(980,1253)" fill="none" stroke="var(--green)" stroke-width="4" stroke-linejoin="round">
      <path d="M-52,-2 L10,-38 L52,-14 L-10,22 Z"/>
      <path d="M-32,-10 L-4,-26 M-24,-5 L4,-21 M-16,0 L12,-16" stroke-width="5"/>
    </g>
    <use href="#tile-green" x="1100" y="1325"/>
    <g transform="translate(1100,1320)" fill="var(--green)">
      <path d="M-32,14 L-14,4 Q-16,-26 4,-32 Q22,-32 24,-12 L36,-2 Z"/>
      <circle cx="38" cy="-14" r="9"/>
    </g>
    <use href="#tile-green" x="1222" y="1395"/>
    <g transform="translate(1222,1392) scale(1,0.9) rotate(-30)" fill="none" stroke="var(--green)" stroke-width="6">
      <path d="M-40,0 Q0,-34 40,0 Q0,34 -40,0 Z"/>
      <circle r="12" fill="var(--green)"/>
    </g>
  </g>

  <!-- external data outputs -->
  <g class="modules-other">
    <use href="#tile-navy" x="2048" y="1270"/>
    <g transform="translate(2048,1262)" fill="var(--navy)" stroke="var(--face)" stroke-width="3">
      <path d="M-30,10 L0,-6 L30,10 L0,26 Z"/>
      <path d="M-30,-2 L0,-18 L30,-2 L0,14 Z"/>
      <path d="M-30,-14 L0,-30 L30,-14 L0,2 Z"/>
    </g>
    <use href="#tile-navy" x="1918" y="1345"/>
    <path d="M1870,1345 L1915,1320 L1960,1345 L1915,1370 Z" fill="var(--navy)"/>
    <use href="#tile-navy" x="1788" y="1420"/>
    <g transform="translate(1788,1418)" fill="none" stroke="var(--navy)" stroke-width="4" stroke-linejoin="round">
      <path d="M-52,-2 L10,-38 L52,-14 L-10,22 Z"/>
      <path d="M-20,4 L20,-19 M-10,9 L30,-14 M-30,-2 L10,-25" stroke-width="3"/>
    </g>
  </g>
</svg>

<ul class="legend">
  <li class="legend-item legend-item--ours"><span class="legend-swatch"></span>Our Software</li>
  <li class="legend-item legend-item--other"><span class="legend-swatch"></span>Other Software</li>
</ul>
</main>
</body>
</html>
```